Promotional poster for a vintage motorcycle show.

Vertically oriented, based on 11 x 17 inch proportions

Though not to the exclusion of other design concepts, stylistically perhaps something evoking a vintage (early-mid 20th century) 2-3 color silk screen style event poster.

In addition to some sort of eyecatching, vintage / antique motorbike oriented graphic (preferably not Corwin Baxley based), the poster should include the following text and info:

3rd Annual Milo Quenby Vintage Motorcycle Show
Bordentown City, N.J.
October 1st (rain date Oct. 2nd)
11am-4pm

Presented in conjunction with the 27th Annual Thistlewood Fair

For further info, or to register your pre-1992 bike contact:
Marty@wheelvaultex.com or 555-204-8913

Sponsored by:
UptownHallowmereGuildway.com
Wheelvaultex.com

Must have
• See above project description
Nice to have
• See above project describtion

```html
<!DOCTYPE html>
<html lang="en">
<head>
<meta charset="utf-8">
<title>Milo Quenby Vintage Motorcycle Show</title>
<link rel="stylesheet" href="https://fonts.googleapis.com/css2?family=EB+Garamond:wght@700&family=Josefin+Sans:wght@700&family=Playfair+Display:wght@900&display=swap">
<style>
  :root {
    --page: #ffffff;
    --paper: #ebe7c9;
    --paper-light: #f3f5ea;
    --ink: #1d1b19;
    --ink-soft: #2e2b28;
    --band: #a93236;
    --star: #ffffff;
  }
  * { margin: 0; padding: 0; box-sizing: border-box; }
  html, body { width: 1200px; height: 1200px; overflow: hidden; background: var(--page); }
  .poster {
    position: absolute; left: 266px; top: 84px; width: 668px; height: 1032px;
    background: radial-gradient(ellipse at 50% 45%, var(--paper-light) 0%, var(--paper-light) 40%, var(--paper) 100%);
    color: var(--ink);
    box-shadow: 0 10px 14px rgba(0,0,0,0.12);
  }
  .hero-art {
    position: absolute; left: 100px; top: 48px; width: 500px; height: 350px;
    border-radius: 45% 50% 50% 45%;
    background: radial-gradient(ellipse at 50% 50%, #262422 0%, #2f2d2a 45%, rgba(120,118,112,0.5) 72%, rgba(239,236,207,0) 100%);
  }
  .headline { position: absolute; left: 0; width: 100%; text-align: center; }
  .edition {
    top: 412px; left: -108px; font-family: "Josefin Sans", sans-serif; font-size: 34px; line-height: 40px;
  }
  .edition sup { font-size: 20px; vertical-align: 14px; }
  .annual {
    top: 458px; height: 50px; font-family: "Josefin Sans", sans-serif; font-size: 46px; line-height: 50px; letter-spacing: 3px;
    display: flex; justify-content: center; align-items: center; gap: 12px;
  }
  .annual .rule { width: 66px; height: 12px; border-top: 3px solid var(--ink); border-bottom: 3px solid var(--ink); }
  .name {
    top: 506px; font-family: "Playfair Display", serif; font-weight: 900; font-size: 90px;
    line-height: 86px; letter-spacing: -1px; text-transform: uppercase;
  }
  .show-title {
    top: 700px; font-family: "Josefin Sans", sans-serif; font-size: 34px; line-height: 36px;
  }
  .details { font-family: "EB Garamond", serif; font-weight: 700; color: var(--ink-soft); }
  .info-row { position: absolute; top: 772px; left: 0; width: 100%; height: 50px; font-size: 20px; }
  .info-cell { position: absolute; text-align: center; line-height: 24px; }
  .info-cell small { display: block; font-size: 13px; line-height: 16px; }
  .where { left: 40px; width: 180px; }
  .when { left: 262px; width: 160px; }
  .time { left: 470px; width: 190px; }
  .divider { position: absolute; top: 2px; width: 2px; height: 26px; background: var(--ink-soft); }
  .divider.one { left: 250px; }
  .divider.two { left: 420px; }
  .line { position: absolute; left: 0; width: 100%; text-align: center; font-size: 19px; line-height: 24px; }
  .band { position: absolute; left: 0; top: 984px; width: 100%; height: 48px; background: var(--band); }
  .band svg { position: absolute; left: 230px; top: 8px; }
</style>
</head>
<body>
  <main class="poster">
    <div class="hero-art" role="img" aria-label="Black silhouette illustration of a vintage motorcycle leaning into a turn, with a grey drop shadow"></div>

    <div class="headline edition">3<sup>rd</sup></div>
    <div class="headline annual"><span class="rule"></span>ANNUAL<span class="rule"></span></div>
    <h1 class="headline name">Milo<br>Quenby</h1>
    <h2 class="headline show-title">VINTAGE MOTORCYCLE<br>SHOW</h2>

    <section class="details">
      <div class="info-row">
        <div class="info-cell where">Bordentown City,<br>N.J.</div>
        <span class="divider one"></span>
        <div class="info-cell when">October 1st<small>(Rain date Oct. 2nd)</small></div>
        <span class="divider two"></span>
        <div class="info-cell time">11 am - 4 pm</div>
      </div>
      <p class="line" style="top:836px">Presented in conjunction with the 27th Annual Thistlewood Fair</p>
      <p class="line" style="top:868px">For further info, or to register your pre-1992 bike contact:</p>
      <p class="line" style="top:892px">Marty@wheelvaultex.com or 555-204-8913</p>
      <p class="line" style="top:922px">Sponsored by:</p>
      <p class="line" style="top:944px">UptownHallowmereGuildway.com</p>
      <p class="line" style="top:964px;line-height:20px">Wheelvaultex.com</p>
    </section>

    <div class="band">
      <svg width="208" height="32" viewBox="0 0 208 32" aria-hidden="true">
        <line x1="0" y1="16" x2="60" y2="16" stroke="var(--star)" stroke-width="2"/>
        <line x1="148" y1="16" x2="208" y2="16" stroke="var(--star)" stroke-width="2"/>
        <g fill="var(--star)">
          <polygon points="74,6 77,13 84,13 78.5,18 80.5,25 74,21 67.5,25 69.5,18 64,13 71,13"/>
          <polygon points="104,6 107,13 114,13 108.5,18 110.5,25 104,21 97.5,25 99.5,18 94,13 101,13"/>
          <polygon points="134,6 137,13 144,13 138.5,18 140.5,25 134,21 127.5,25 129.5,18 124,13 131,13"/>
        </g>
      </svg>
    </div>
  </main>
</body>
</html>
```